Web Design for Financial Consulting Company

We need a website design for a financial consulting company "Kelvane Consulting". We build financial models, scenario analysis, handle the budgeting process and provide temporary staffing. I have over 10 years of experience. My Excel expertise and analytical savvy has saved clients over $17 million in profit.

Target Market(s)

Small to medium businesses

Industry/Entity Type

Financial Consulting

Number of Pages Required

4 page

Requirements
Must have
• Professional looking
Nice to have
• A little futuristic looking

```html
<!DOCTYPE html>
<html lang="en">
<head>
<meta charset="utf-8">
<title>Kelvane Consulting</title>
<link href="https://fonts.googleapis.com/css2?family=Poppins:wght@400;500;600;700&display=swap" rel="stylesheet">
<style>
:root{
  --blue:#0aa8ea;
  --navy:#123e69;
  --footer:#053f6b;
  --muted:#6a4e6a;
  --text:#333;
  --card-shadow:0 8px 22px rgba(0,0,0,.12);
}
*{box-sizing:border-box;margin:0;padding:0}
html,body{width:1200px;height:3045px;overflow:hidden}
body{font-family:'Poppins',sans-serif;background:#fff;color:var(--text);position:relative}
.topbar{height:14px;background:var(--blue)}
.header{height:96px;position:relative;box-shadow:0 2px 6px rgba(0,0,0,.05)}
.brand{position:absolute;left:44px;top:34px;display:flex;align-items:center;gap:12px}
.brand-mark{width:30px;height:30px;background:var(--blue)}
.brand-name{font-size:28px;font-weight:600;color:var(--navy);letter-spacing:1px}
.nav{position:absolute;left:639px;top:40px;display:flex;gap:30px;font-size:16px;font-weight:500}
.nav a{color:var(--muted);text-decoration:none}
.nav a.active{color:var(--blue)}
.callus{position:absolute;right:42px;top:30px;display:flex;align-items:center;gap:8px;text-align:right;font-size:15px;color:#444;line-height:18px}
.hero{height:704px;background:linear-gradient(135deg,#1c2533 0%,#3d4b5e 45%,#7d8796 75%,#3a4555 100%);position:relative;display:flex;align-items:center;justify-content:center}
.hero h1{color:#fff;font-size:51px;font-weight:700;line-height:66px;text-align:center;margin-top:-30px}
.about{height:457px;background:linear-gradient(180deg,#dcdfe4,#f2f2f4 60%,#e8e8ea);position:relative;text-align:center}
.section-title{display:inline-block;font-size:34px;font-weight:700;color:var(--navy);border-bottom:3px solid var(--blue);padding:0 4px 2px 60px;line-height:40px}
.about .section-title{margin-top:150px}
.about p{width:960px;margin:62px auto 0;font-size:16px;letter-spacing:1px;line-height:39px;color:#222}
.services{height:1279px;position:relative;text-align:center;background:#fff}
.services .section-title{margin-top:82px;color:var(--blue)}
.card{position:absolute;background:#fff;box-shadow:var(--card-shadow);display:flex;text-align:left}
.card .photo{width:228px;height:100%;flex:none}
.card .body{padding:0 14px 0 34px;display:flex;flex-direction:column;justify-content:center}
.card h3{font-size:18.5px;font-weight:600;color:var(--navy);line-height:22px;margin-bottom:22px;white-space:nowrap}
.card p{font-size:15.5px;line-height:19px;color:#555}
.card.active{border:3px solid var(--blue)}
.footer{position:absolute;top:2550px;left:0;width:1200px;height:495px;background:var(--footer);color:#fff;text-align:center}
.footer .brand-f{display:inline-flex;align-items:center;gap:14px;margin-top:70px}
.footer .brand-f .brand-mark{width:40px;height:40px;background:#fff}
.footer .brand-f span{font-size:42px;font-weight:600;letter-spacing:2px}
.f-head{font-size:15px;font-weight:600;text-decoration:underline;text-underline-offset:4px;margin-top:42px}
.f-links{display:flex;justify-content:center;gap:22px;font-size:15px;margin-top:14px}
.f-contacts{display:flex;justify-content:center;gap:26px;margin-top:22px;text-align:left;font-size:15px;line-height:19px}
.f-contacts .item{display:flex;align-items:center;gap:12px}
.socials{display:flex;justify-content:center;gap:22px;margin-top:42px}
.socials span{width:18px;height:18px;background:var(--blue);display:block}
</style>
</head>
<body>
<div class="topbar"></div>
<header class="header">
  <div class="brand"><span class="brand-mark"></span><span class="brand-name">Kelvane Consulting</span></div>
  <nav class="nav"><a class="active">Home</a><a>About Us</a><a>Service</a><a>Contact</a></nav>
  <div class="callus"><div>CALL US<br>0123 555 0147</div>
    <svg width="34" height="34" viewBox="0 0 34 34"><circle cx="17" cy="17" r="15" fill="none" stroke="#123e69" stroke-width="2"/><path d="M11 10c1-1 2-1 3 0l2 3c0 1 0 2-1 2l-1 1c1 2 3 4 5 5l1-1c1-1 2-1 2 0l3 2c1 1 1 2 0 3-2 2-5 1-9-3s-6-8-5-12z" fill="none" stroke="#123e69" stroke-width="1.8"/></svg>
  </div>
</header>

<section class="hero" role="img" aria-label="Photo of business people reviewing financial charts and reports on a desk">
  <h1>Helping Your<br>Finance Team<br>And Increasing Profit</h1>
</section>

<section class="about">
  <div role="img" aria-label="Faded photo of a business meeting around a conference table" style="position:absolute;inset:0;background:linear-gradient(90deg,rgba(200,204,212,.4),rgba(255,255,255,.2),rgba(200,204,212,.4))"></div>
  <div style="position:relative">
    <h2 class="section-title">ABOUT US</h2>
    <p>I am an experienced Finance professional who develops strategic financial plans, provides insightful analysis, and supports decision-making. With over 10 years of experience, I have successfully increased profitability for clients by $17M</p>
  </div>
</section>

<section class="services">
  <h2 class="section-title">SERVICES</h2>

  <div class="card" style="left:111px;top:204px;width:476px;height:276px">
    <div class="photo" role="img" aria-label="Photo of a presenter beside a stock chart screen in a meeting room" style="height:296px;margin-top:-20px;background:linear-gradient(160deg,#dfe5ee,#5a6a86 50%,#8a6a4c)"></div>
    <div class="body"><h3>Financial<br>Models – Projects</h3><p>Financial analysis, scenario modeling, pricing analysis, projects</p></div>
  </div>
  <div class="card" style="left:622px;top:204px;width:476px;height:276px">
    <div class="photo" role="img" aria-label="Photo of hands using a laptop touchpad and tablet" style="background:linear-gradient(160deg,#c9ccd2,#9ea4ad 50%,#e7eaee)"></div>
    <div class="body"><h3>Budgeting Process</h3><p>Building budgets from scratch, revamping current process to be more robust and scalable</p></div>
  </div>
  <div class="card active" style="left:111px;top:539px;width:483px;height:305px">
    <div class="photo" role="img" aria-label="Photo of a hand writing on printed financial charts" style="background:linear-gradient(160deg,#e9e4dc,#b9c4d0 55%,#6fa3d6)"></div>
    <div class="body"><h3>Long Black</h3><p>Years of Financial Planning and Analysis experience across multiple industries can help temporary staffing needs.</p></div>
  </div>
  <div class="card" style="left:628px;top:548px;width:476px;height:296px">
    <div class="photo" role="img" aria-label="Photo of a calculator, tablet and charts on a white desk" style="background:linear-gradient(160deg,#f1f2f4,#b6bcc6 55%,#3a3d44)"></div>
    <div class="body" style="padding-left:20px;padding-right:10px"><h3>Data cleansing</h3><p style="line-height:23px">Lorem ipsum dolor sit amet, consectetur adipiscing elit, sed do eiusmod tempor in-cididunt ut labore et dolore</p></div>
  </div>
  <div class="card" style="left:339px;top:889px;width:477px;height:296px">
    <div class="photo" role="img" aria-label="Photo of a person beside a blue bar chart model" style="background:linear-gradient(160deg,#8a7d70,#d9d6d0 55%,#2f6fc4)"></div>
    <div class="body" style="padding-left:25px;padding-right:8px"><h3>Process Improvement</h3><p style="line-height:20px">Volutpat lacus laoreet non curabitur. Ullamcorper dignissim cras tincidunt lobortis feugiat vivamus at augue eget. Suscipit adipiscing bibendum est ultricies integer</p></div>
  </div>
</section>

<footer class="footer">
  <div class="brand-f"><span class="brand-mark"></span><span>Kelvane Consulting</span></div>
  <div class="f-head">QUICK LINK</div>
  <div class="f-links"><span>HOME</span><span>ABOUT US</span><span>SERVICE</span><span>CONTACT US</span></div>
  <div class="f-head" style="margin-top:40px">CONTACT US</div>
  <div class="f-contacts">
    <div class="item"><svg width="34" height="34" viewBox="0 0 34 34"><circle cx="17" cy="17" r="15" fill="none" stroke="#fff" stroke-width="2"/><path d="M11 10c1-1 2-1 3 0l2 3c0 1 0 2-1 2l-1 1c1 2 3 4 5 5l1-1c1-1 2-1 2 0l3 2c1 1 1 2 0 3-2 2-5 1-9-3s-6-8-5-12z" fill="none" stroke="#fff" stroke-width="1.8"/></svg><div>CALL US<br>0123 555 0147</div></div>
    <div class="item"><svg width="34" height="34" viewBox="0 0 34 34"><circle cx="17" cy="17" r="15" fill="none" stroke="#fff" stroke-width="2"/><rect x="9" y="11" width="16" height="12" fill="none" stroke="#fff" stroke-width="1.8"/><path d="M9 11l8 7 8-7" fill="none" stroke="#fff" stroke-width="1.8"/></svg><div>EMAIL US<br>hello@kelvanemail.com</div></div>
    <div class="item"><svg width="34" height="34" viewBox="0 0 34 34"><circle cx="17" cy="17" r="15" fill="none" stroke="#fff" stroke-width="2"/><path d="M17 26s-6-6-6-11a6 6 0 0 1 12 0c0 5-6 11-6 11z" fill="none" stroke="#fff" stroke-width="1.8"/><circle cx="17" cy="15" r="2" fill="#fff"/></svg><div>Address Line Dummy Here<br>Dummy Address Here</div></div>
  </div>
  <div class="socials"><span></span><span></span><span></span></div>
</footer>
</body>
</html>
```